The Kestrowe Banner Ad

The Kestrowe (www.thekestrowe.example) is a news-based website in South China that also features dining and nightlife listings, events, jobs, classifieds and more. The cities we cover are Guangzhou and Shenzhen. We have the rare opportunity to have an advertisement placed on the website of the leading English newspaper in Asia. It is a captive audience of people already reading news, so we want to draw their attention to an alternative site for information.

The ad copy is:

Want more China?
The latest news, dining, nightlife, and jobs.
Guangzhou and Shenzhen
The Kestrowe (with a button saying "Check it out")

(Or something like that... you have freedom to adjust the wording).

The dimensions are 300 x 250 px, with a file size <30kb in JPEG/Animated GIF.

```html
<!DOCTYPE html>
<html lang="en">
<head>
<meta charset="utf-8">
<title>The Kestrowe Banner Ad Concepts</title>
<link rel="stylesheet" href="https://fonts.googleapis.com/css2?family=Roboto+Condensed:wght@400;500&family=Titillium+Web:wght@400;600;700&display=swap">
<style>
  :root {
    --stage: #0c0c0c;
    --red-deep: #8e0000;
    --red: #c40d0d;
    --red-bright: #ee2424;
    --white: #ffffff;
    --ink: #1a1a1a;
    --yellow: #fff200;
    --orange-top: #ffad2e;
    --orange-bottom: #dd5e00;
    --sky-top: #2f8fd0;
    --sky-mid: #9aa6c2;
    --city-low: #3c4656;
    --city-lights: #5b4a3e;
  }
  * { box-sizing: border-box; margin: 0; padding: 0; }
  html, body {
    width: 1200px; height: 496px; overflow: hidden;
    background: var(--stage);
  }
  .stage { position: relative; width: 1200px; height: 496px; }

  .banner {
    position: absolute; top: 112px;
    width: 320px; height: 266px;
    overflow: hidden; background: var(--white);
    box-shadow: 0 4px 14px rgba(0,0,0,.6);
  }
  .banner--split { left: 62px; }
  .banner--overlay { left: 434px; }
  .banner--wave { left: 802px; }

  .city-photo {
    position: absolute; left: 0; top: 0; width: 320px; height: 208px;
    background: linear-gradient(180deg, var(--sky-top) 0%, var(--sky-mid) 38%, var(--city-low) 62%, var(--city-lights) 82%, #2a2f3a 100%);
  }

  .footer-bar {
    position: absolute; left: 0; top: 208px; width: 320px; height: 58px;
    background: var(--white);
  }
  .brand-name {
    position: absolute; left: 8px; top: 16px;
    display: flex; align-items: center; gap: 6px;
    font-family: "Titillium Web", sans-serif; font-weight: 600;
    font-size: 21px; color: var(--ink); line-height: 1;
  }
  .brand-name::before {
    content: ""; width: 9px; height: 9px; border-radius: 50%;
    background: var(--red);
  }
  .cta-button {
    position: absolute; left: 178px; top: 14px; width: 137px; height: 34px;
    border-radius: 5px;
    background: linear-gradient(180deg, var(--orange-top), var(--orange-bottom));
    box-shadow: 0 2px 3px rgba(0,0,0,.35);
    display: flex; align-items: center; justify-content: center; gap: 5px;
    font-family: "Titillium Web", sans-serif; font-weight: 600; font-size: 15px;
    color: var(--white); text-shadow: 0 1px 1px rgba(0,0,0,.35);
    white-space: nowrap;
  }
  .cta-button svg { width: 16px; height: 16px; }

  /* split concept */
  .red-panel { position: absolute; left: 0; top: 0; width: 320px; height: 208px; }
  .split-copy {
    position: absolute; left: 170px; top: 6px; width: 142px;
    text-align: center; font-family: "Roboto Condensed", sans-serif;
    color: var(--white); white-space: nowrap;
  }
  .split-copy .kicker { font-size: 28px; font-weight: 500; line-height: 30px; letter-spacing: -1.2px; }
  .split-copy .headline { font-size: 42px; font-weight: 500; line-height: 40px; letter-spacing: -1px; }
  .split-copy .rule { height: 1px; margin: 5px 8px 6px; background: rgba(0,0,0,.35); }
  .split-copy .tagline { font-size: 17px; line-height: 19px; }
  .split-copy .cities { margin-top: 6px; font-size: 18px; line-height: 19px; color: var(--yellow); }

  /* overlay & wave concepts */
  .display-copy { position: absolute; font-family: "Titillium Web", sans-serif; color: var(--white); text-shadow: 0 2px 3px rgba(0,0,0,.45); white-space: nowrap; }
  .display-copy .headline { font-size: 28px; font-weight: 700; line-height: 1; letter-spacing: -.5px; }
  .display-copy .tagline { font-weight: 600; line-height: 1.05; }
  .banner--overlay .display-copy { left: 0; top: 9px; width: 320px; text-align: center; }
  .banner--overlay .tagline { font-size: 20px; margin-top: 3px; }
  .banner--wave .display-copy { left: 11px; top: 9px; }
  .banner--wave .tagline { font-size: 18px; font-weight: 400; margin-top: 3px; }
  .wave-band { position: absolute; left: 0; top: 0; width: 320px; height: 208px; }
  .cities-strip {
    position: absolute; left: 5px; top: 185px;
    font-family: "Titillium Web", sans-serif; font-weight: 700; font-size: 16px;
    color: var(--yellow); text-shadow: 0 1px 2px rgba(0,0,0,.6); white-space: nowrap;
  }
  .banner--wave .cities-strip { top: 187px; }
</style>
</head>
<body>
<main class="stage">

  <section class="banner banner--split">
    <div class="city-photo" role="img" aria-label="Evening skyline of Guangzhou with a lit stadium"></div>
    <svg class="red-panel" viewBox="0 0 320 208" aria-hidden="true">
      <defs>
        <linearGradient id="panelRed" x1="0" y1="0" x2="0" y2="1">
          <stop offset="0" stop-color="var(--red)"/>
          <stop offset="1" stop-color="var(--red-deep)"/>
        </linearGradient>
      </defs>
      <path d="M130 0 Q178 90 166 208 L320 208 L320 0 Z" fill="var(--white)"/>
      <path d="M136 0 Q184 90 172 208 L320 208 L320 0 Z" fill="url(#panelRed)"/>
    </svg>
    <div class="split-copy">
      <p class="kicker">WANT MORE</p>
      <p class="headline">CHINA?</p>
      <div class="rule"></div>
      <p class="tagline">The latest news,<br>dining, nightlife<br>and jobs.</p>
      <p class="cities">GUANGZHOU<br>AND SHENZHEN</p>
    </div>
    <div class="footer-bar">
      <span class="brand-name">The Kestrowe</span>
      <span class="cta-button">CHECK IT OUT
        <svg viewBox="0 0 16 16" aria-hidden="true"><circle cx="8" cy="8" r="7.5" fill="#fff"/><path d="M6.5 4.5 L10 8 L6.5 11.5" fill="none" stroke="#b65a10" stroke-width="2"/></svg>
      </span>
    </div>
  </section>

  <section class="banner banner--overlay">
    <div class="city-photo" role="img" aria-label="Evening skyline of Guangzhou with a lit stadium"></div>
    <div class="display-copy">
      <p class="headline">WANT MORE CHINA?</p>
      <p class="tagline">The latest news, dining,<br>nightlife and jobs.</p>
    </div>
    <p class="cities-strip">GUANGZHOU AND SHENZHEN</p>
    <div class="footer-bar">
      <span class="brand-name">The Kestrowe</span>
      <span class="cta-button">CHECK IT OUT
        <svg viewBox="0 0 16 16" aria-hidden="true"><circle cx="8" cy="8" r="7.5" fill="#fff"/><path d="M6.5 4.5 L10 8 L6.5 11.5" fill="none" stroke="#b65a10" stroke-width="2"/></svg>
      </span>
    </div>
  </section>

  <section class="banner banner--wave">
    <div class="city-photo" role="img" aria-label="Evening skyline of Guangzhou with a lit stadium"></div>
    <svg class="wave-band" viewBox="0 0 320 208" aria-hidden="true">
      <defs>
        <linearGradient id="waveRed" x1="0" y1="0" x2="1" y2="1">
          <stop offset="0" stop-color="var(--red)"/>
          <stop offset="1" stop-color="var(--red-bright)"/>
        </linearGradient>
      </defs>
      <path d="M0 0 H320 V70 Q150 76 0 130 Z" fill="#f35a5a"/>
      <path d="M0 0 H320 V66 Q150 70 0 124 Z" fill="url(#waveRed)"/>
    </svg>
    <div class="display-copy">
      <p class="headline">WANT MORE CHINA?</p>
      <p class="tagline">The latest news, dining,<br>nightlife and jobs.</p>
    </div>
    <p class="cities-strip">GUANGZHOU AND SHENZHEN</p>
    <div class="footer-bar">
      <span class="brand-name">The Kestrowe</span>
      <span class="cta-button">CHECK IT OUT
        <svg viewBox="0 0 16 16" aria-hidden="true"><circle cx="8" cy="8" r="7.5" fill="#fff"/><path d="M6.5 4.5 L10 8 L6.5 11.5" fill="none" stroke="#b65a10" stroke-width="2"/></svg>
      </span>
    </div>
  </section>

</main>
</body>
</html>
```